Need web design for our e-assessment company

We need a web design for our e-assessment company called Tavelo. We develop modern, web-based software for supporting the testing and examination process. The application is delivered as a SaaS solution.

The application helps our customers save time and money.

The design should communicate the following:

- Modern
- Innovation
- Security
- Performance

Attached you can find a screenshot of our application as well as some thoughts on the website.

We would like a front page as well as 1 sub page.

And lastly, one more website we draw inspiration from (on top of the ones mentioned in the attached document): http://www.plonkavery.example/
Updates

Dear all,

I have updated the description with 1 more example of websites we like as well as added that we would like a front page and a sub page.

Thanks in advance.

Best regards,

Torlak

Target Market(s)

Our target groups are higher education and awarding organisations. Decision makers are mostly men age 45+.

Industry/Entity Type

It Company

Requirements
Must have
• 1 front page and 1 sub page

```html
<!DOCTYPE html>
<html lang="en">
<head>
<meta charset="utf-8">
<title>Tavelo – e-Assessment made simple</title>
<link href="https://fonts.googleapis.com/css2?family=Open+Sans:wght@400;600;700&family=Roboto:wght@300;400;500;700&display=swap" rel="stylesheet">
<style>
:root{
  --orange:#e2621b;
  --orange-dark:#c9530f;
  --blue:#2d7fc3;
  --green:#3f9a2e;
  --ink:#2b2b2b;
  --text:#666;
  --muted:#999;
  --line:#e3e3e3;
  --band:#f1f1f1;
  --footer:#262626;
  --footer-bar:#1b1b1b;
  --white:#fff;
  --teal-dark:#0f2e3a;
}
*{margin:0;padding:0;box-sizing:border-box}
html,body{width:1200px;height:2332px;overflow:hidden}
body{font-family:"Open Sans",Arial,sans-serif;color:var(--text);background:var(--white);font-size:13px;line-height:1.6}
a{color:inherit;text-decoration:none}
.wrap{width:840px;margin:0 auto;position:relative}

/* header */
.site-header{height:72px;display:flex;align-items:center;justify-content:space-between;padding:0 52px;background:var(--white)}
.brand{display:flex;align-items:center;gap:12px;font-family:"Roboto",sans-serif;font-size:30px;font-weight:500;color:var(--ink)}
.brand-mark{width:34px;height:34px;background:var(--orange);border-radius:4px}
.main-nav{display:flex;align-items:center;gap:44px;font-family:"Roboto",sans-serif;font-size:14px;color:var(--ink)}
.main-nav .active{color:var(--orange);border-bottom:2px solid var(--orange);padding-bottom:4px}
.btn-login{background:var(--ink);color:var(--white);padding:8px 20px;border-radius:3px;font-size:13px}

/* hero */
.hero{height:528px;position:relative;background:radial-gradient(ellipse at 70% 45%,#8a6a4c 0%,#5a4030 35%,#2c1f18 75%,#1c1410 100%)}
.hero-text{position:absolute;left:180px;top:420px;color:var(--white)}
.hero-text h1{font-family:"Roboto",sans-serif;font-weight:400;font-size:27px;margin-bottom:14px}
.btn{display:inline-block;font-family:"Roboto",sans-serif;font-size:12px;font-weight:500;text-transform:uppercase;color:var(--white);padding:10px 22px;border-radius:2px;margin-right:8px}
.btn-blue{background:var(--blue)}
.btn-orange{background:var(--orange)}
.slider-dots{position:absolute;bottom:12px;left:50%;transform:translateX(-50%);display:flex;gap:8px}
.slider-dots span{width:10px;height:10px;border-radius:50%;background:rgba(255,255,255,.5)}
.slider-dots span.on{background:var(--white)}

/* features */
.features{padding:50px 0 0}
.section-title{text-align:center;font-family:"Roboto",sans-serif;font-size:28px;font-weight:400;color:var(--ink)}
.feature-row{display:flex;justify-content:space-between;margin-top:44px;padding:0 20px}
.feature{width:240px;text-align:center}
.feature-icon{width:112px;height:112px;border-radius:50%;margin:0 auto 18px;display:flex;align-items:center;justify-content:center;box-shadow:0 0 0 6px #ececec}
.feature-icon.blue{background:var(--blue)}
.feature-icon.orange{background:var(--orange)}
.feature-icon.green{background:var(--green)}
.feature h3{font-family:"Roboto",sans-serif;font-size:16px;font-weight:500;color:var(--ink);margin-bottom:8px}
.feature p{font-size:11px;line-height:1.6}

/* promo banner */
.promo{margin-top:60px;height:222px;display:flex;background:linear-gradient(90deg,#0d2b38,#123b4a);border-bottom:4px solid var(--blue)}
.promo-copy{width:420px;padding:28px 36px;color:#cfe3ea}
.promo-copy h2{font-family:"Roboto",sans-serif;font-weight:500;font-size:24px;color:var(--white);margin-bottom:10px}
.promo-copy p{font-size:11px;margin-bottom:16px}
.promo-visual{flex:1;background:linear-gradient(120deg,#0e3a48 0%,#1b6f86 45%,#0b2c38 100%)}

/* education */
.education{margin-top:48px;background:var(--band);height:320px;padding-top:40px}
.education .wrap{display:flex;justify-content:space-between}
.edu-copy{width:400px}
.edu-copy h2{font-family:"Roboto",sans-serif;font-weight:400;font-size:24px;color:var(--ink);margin-bottom:10px}
.edu-copy .lead{color:var(--orange);font-size:11px;margin-bottom:10px}
.edu-copy p{font-size:11px;margin-bottom:18px}
.edu-visual{width:400px;height:240px;background:linear-gradient(160deg,#f7f7f7,#dcdfe3 60%,#c9ced4)}

/* news */
.news{padding-top:40px}
.news h2{font-family:"Roboto",sans-serif;font-weight:400;font-size:24px;color:var(--ink);margin-bottom:6px}
.news-intro{font-size:11px;width:560px;margin-bottom:16px}
.news-grid{display:flex;gap:16px}
.news-card{width:180px}
.news-thumb{height:112px;margin-bottom:8px}
.news-thumb.t1{background:linear-gradient(135deg,#8a7e70,#c9bfae)}
.news-thumb.t2{background:linear-gradient(135deg,#3a4858,#9fb0bf)}
.news-thumb.t3{background:linear-gradient(135deg,#d7d2cc,#a9342b)}
.news-card p{font-size:11px;line-height:1.5}
.news-video{flex:1;height:196px;margin-top:-56px;position:relative;background:linear-gradient(135deg,#3c3c3c,#7a6a62 50%,#2a2a2a)}
.play{position:absolute;left:50%;top:50%;transform:translate(-50%,-50%)}

/* partners */
.partners{padding-top:58px}
.partners h3{font-family:"Roboto",sans-serif;font-weight:500;font-size:16px;color:var(--ink);margin-bottom:18px}
.partner-row{display:flex;justify-content:space-between;align-items:center}
.partner-badge{width:110px;height:34px;background:#d4d4d4;border-radius:3px}

/* blog + newsletter */
.orange-band{margin-top:52px;background:var(--orange);height:100px;color:var(--white)}
.orange-band .wrap{display:flex;justify-content:space-between;align-items:center;height:100px}
.blog{display:flex;gap:14px;align-items:center}
.blog-thumb{width:80px;height:60px;background:linear-gradient(135deg,#f3c9a8,#b5531c)}
.blog h4,.newsletter h4{font-family:"Roboto",sans-serif;font-size:15px;font-weight:500;margin-bottom:4px}
.blog p{font-size:11px;width:260px;line-height:1.5}
.newsletter{width:340px}
.signup{display:flex}
.signup span{flex:1;background:var(--white);color:var(--muted);font-size:11px;padding:7px 10px}
.signup b{background:var(--blue);font-size:11px;font-weight:600;padding:7px 16px}

/* footer */
.site-footer{background:var(--footer);height:180px;color:#aaa;padding-top:26px}
.site-footer .wrap{display:flex}
.foot-col{width:210px;font-size:11px}
.foot-col h5{font-family:"Roboto",sans-serif;font-size:14px;font-weight:500;color:var(--white);margin-bottom:10px}
.foot-col li{list-style:none;line-height:1.9;display:flex;align-items:center;gap:8px}
.dot{width:10px;height:10px;background:var(--orange);border-radius:2px;display:inline-block}
.foot-bar{background:var(--footer-bar);height:32px;color:#888;font-size:10px}
.foot-bar .wrap{display:flex;justify-content:space-between;align-items:center;height:32px}
</style>
</head>
<body>

<header class="site-header">
  <a class="brand" href="#"><span class="brand-mark"></span>Tavelo</a>
  <nav class="main-nav">
    <a class="active" href="#">Home</a>
    <a href="#">Products</a>
    <a href="#">Features</a>
    <a href="#">Pricing</a>
    <a href="#">Contact Us</a>
    <a class="btn-login" href="#">Login</a>
  </nav>
</header>

<section class="hero" role="img" aria-label="Person holding a tablet showing the Tavelo assessment dashboard">
  <div class="hero-text">
    <h1>No servers. No maintenance. No worries</h1>
    <a class="btn btn-blue" href="#">Learn more</a><a class="btn btn-orange" href="#">Free trial</a>
  </div>
  <div class="slider-dots"><span class="on"></span><span></span><span></span></div>
</section>

<section class="features">
  <h2 class="section-title">“e-Assessment made simple”</h2>
  <div class="wrap">
    <div class="feature-row">
      <div class="feature">
        <div class="feature-icon blue"><svg width="44" height="44" viewBox="0 0 44 44"><path d="M22 4l5.5 11.5 12.5 1.6-9.2 8.7 2.3 12.4L22 32.2 10.9 38.2l2.3-12.4L4 17.1l12.5-1.6z" fill="#fff"/></svg></div>
        <h3>Awesome Feature</h3>
        <p>Create secure exams in minutes and deliver them to every candidate on any device they prefer to use.</p>
      </div>
      <div class="feature">
        <div class="feature-icon orange"><svg width="44" height="44" viewBox="0 0 44 44"><circle cx="22" cy="22" r="8" fill="none" stroke="#fff" stroke-width="5"/><path d="M22 4v8M22 32v8M4 22h8M32 22h8M9 9l6 6M29 29l6 6M9 35l6-6M29 15l6-6" stroke="#fff" stroke-width="5"/></svg></div>
        <h3>Customizable</h3>
        <p>Adapt question types, grading rules and branding so every test fits the way your institution works.</p>
      </div>
      <div class="feature">
        <div class="feature-icon green"><svg width="44" height="44" viewBox="0 0 44 44"><path d="M11 5h16l8 8v26H11z" fill="#fff"/><path d="M16 20h14M16 26h14M16 32h10" stroke="#3f9a2e" stroke-width="2.5"/></svg></div>
        <h3>Documented</h3>
        <p>Clear guides and reference pages help staff set up assessments and answer questions quickly.</p>
      </div>
    </div>

    <div class="promo">
      <div class="promo-copy">
        <h2>Lorem ipsum dolor sit amet</h2>
        <p>Our platform runs in the cloud with full encryption, so results stay safe while your team focuses on teaching. Scale from a single class to national exams without extra hardware, downtime or costly upgrades.</p>
        <a class="btn btn-orange" href="#">Learn more</a>
      </div>
      <div class="promo-visual" role="img" aria-label="Glowing streams of binary code"></div>
    </div>
  </div>
</section>

<section class="education">
  <div class="wrap">
    <div class="edu-copy">
      <h2>Education users</h2>
      <p class="lead">Universities and awarding bodies trust Tavelo to run fair, reliable exams from start to finish.</p>
      <p>Plan tests, invite candidates and mark answers in one place. Automatic scoring saves hours for examiners, while detailed reports show how every group performs. Everything runs in the browser, so there is nothing to install and no servers to maintain.</p>
      <a class="btn btn-blue" href="#">Getting started</a><a class="btn btn-orange" href="#">Free trial</a>
    </div>
    <div class="edu-visual" role="img" aria-label="Monitor, laptop, tablet and phone showing the Tavelo application"></div>
  </div>
</section>

<section class="news">
  <div class="wrap">
    <h2>Latest News</h2>
    <p class="news-intro">Read the newest updates from our team, including product releases, customer stories and events where you can meet us in person this season.</p>
    <div class="news-grid">
      <div class="news-card"><div class="news-thumb t1" role="img" aria-label="Students writing an exam"></div><p>New question editor makes building tests faster.</p></div>
      <div class="news-card"><div class="news-thumb t2" role="img" aria-label="Hands typing on a laptop"></div><p>Meet our team at the spring education summit.</p></div>
      <div class="news-card"><div class="news-thumb t3" role="img" aria-label="Desk with notebook and coffee"></div><p>How one college cut grading time in half.</p></div>
      <div class="news-video" role="img" aria-label="Video of a speaker presenting at a conference">
        <svg class="play" width="56" height="56" viewBox="0 0 56 56"><circle cx="28" cy="28" r="28" fill="#e2621b"/><path d="M22 17l17 11-17 11z" fill="#fff"/></svg>
      </div>
    </div>
  </div>
</section>

<section class="partners">
  <div class="wrap">
    <h3>Our Partner</h3>
    <div class="partner-row">
      <span class="partner-badge"></span><span class="partner-badge"></span><span class="partner-badge"></span><span class="partner-badge"></span><span class="partner-badge"></span><span class="partner-badge"></span>
    </div>
  </div>
</section>

<section class="orange-band">
  <div class="wrap">
    <div class="blog">
      <div class="blog-thumb" role="img" aria-label="Blog post photo"></div>
      <div><h4>From Our Blog</h4><p>Five simple ways to make online exams more secure for every candidate.</p></div>
    </div>
    <div class="newsletter">
      <h4>Newsletter Signup</h4>
      <div class="signup"><span>Email address</span><b>SUBMIT</b></div>
    </div>
  </div>
</section>

<footer class="site-footer">
  <div class="wrap">
    <div class="foot-col"><h5>Quick Links</h5><ul><li>Our Products</li><li>Features</li><li>Pricing</li><li>Contact</li></ul></div>
    <div class="foot-col"><h5>Help &amp; Support</h5><ul><li>FAQs</li><li>Live Support</li><li>Send Mail</li></ul></div>
    <div class="foot-col"><h5>Social Connection</h5><ul><li><span class="dot"></span>Community</li><li><span class="dot"></span>Updates</li><li><span class="dot"></span>Network</li><li><span class="dot"></span>Blog</li></ul></div>
    <div class="foot-col"><h5>Get in touch</h5><ul>
      <li><svg width="10" height="10" viewBox="0 0 10 10"><path d="M2 0l2 3-1 1a6 6 0 003 3l1-1 3 2-1 2C4 10 0 6 0 1z" fill="#e2621b"/></svg>123 456 789</li>
      <li><svg width="10" height="10" viewBox="0 0 10 10"><rect y="2" width="10" height="7" fill="#e2621b"/><path d="M0 2l5 4 5-4" stroke="#262626" fill="none"/></svg>hello@tavelo.example</li>
      <li><svg width="10" height="10" viewBox="0 0 10 10"><path d="M5 0a3.5 3.5 0 013.5 3.5C8.5 6 5 10 5 10S1.5 6 1.5 3.5A3.5 3.5 0 015 0z" fill="#e2621b"/></svg>12 Sample Street, Townsville</li>
    </ul></div>
  </div>
</footer>
<div class="foot-bar">
  <div class="wrap"><span>Home | Sitemap | Privacy Policy | Contact</span><span>Copyright © 2014 Tavelo. All rights reserved</span></div>
</div>

</body>
</html>
```